Re-style home page - eye-catching and unique design for social commerce website

We need a new concept design for TrindaMo's home page.
We don't want to make huge changes but creating a more professional and eye-catching style.

We need to look very serious like a professional services company and in the same time to look like a social network for e-commerce.

Our logo is very captive and you can use to creating something of harmonious.

This is a re-style and I'm excepted to see unique and fresh design like Clovaret.

Target Market(s)

e-commerce and social

Industry/Entity Type

Social

Number of Pages Required

1 page

Font styles to use
Serif
Sans Serif

Requirements
Must have
• An eye-catching result.
• Search bar with logo and Login How it works and business
• The slogan with login and signup.
• Footer links.
Nice to have
• I would like to open the home page and see only two clear ways:
• -Consumer
• --Search
• --The slogan
• --Login and Signup
• --How it works
• -Business
• --Go to Business area
• Background: City, Shopping.
Should not have
• Scrollbar style!

```html
<!DOCTYPE html>
<html lang="en">
<head>
<meta charset="utf-8">
<title>TrindaMo – Shop directly from your profile</title>
<link rel="stylesheet" href="https://fonts.googleapis.com/css2?family=Ubuntu:wght@400;500;700&family=Open+Sans:wght@400;600;700&display=swap">
<style>
  :root {
    --ink: #1e1e1e;
    --paper: #fbfbe8;
    --panel: rgba(40, 40, 40, 0.86);
    --footer: #262626;
    --search-bg: #ececec;
    --search-btn: #f0d52c;
    --link-blue: #2a9be8;
    --friendora: #4a68ad;
    --t-crimson: #c8345a;
    --t-blue: #2f3fc4;
    --t-amber: #d9a21a;
    --t-orange: #e0522e;
    --t-tan: #dc8f2c;
    --t-periwinkle: #5a69d8;
    --t-olive: #b8b43a;
    --t-violet: #6f72d8;
    --t-red: #d23a4a;
    --t-mustard: #d4b42a;
    --t-copper: #dc8a2e;
    --t-gold: #e0a70e;
    --t-moss: #9aa64a;
    --t-navy: #3f4e9a;
    --t-salmon: #e0807a;
    --t-coral: #e07a6a;
    --t-flame: #e3572e;
    --t-indigo: #3c4fa0;
    --t-bronze: #a08a16;
    --t-rose: #e0304a;
    --join: #f5d000;
  }
  * { box-sizing: border-box; margin: 0; padding: 0; }
  html, body { width: 1200px; height: 878px; overflow: hidden; }
  body { position: relative; font-family: "Ubuntu", sans-serif; color: var(--ink); background: var(--paper); }

  .backdrop {
    position: absolute; inset: 0 0 55px 0;
    background:
      linear-gradient(180deg, rgba(252,252,230,0.95) 0%, rgba(246,246,214,0.75) 25%, rgba(214,224,200,0.6) 60%, rgba(170,190,200,0.7) 100%),
      linear-gradient(90deg, #c9554a 0%, #d8d6c0 22%, #e8ecd6 50%, #c8d8c2 78%, #9fa9a0 100%);
  }

  .site-header { position: absolute; top: 0; left: 0; width: 1200px; height: 90px; }
  .brand { position: absolute; left: 129px; top: 26px; display: flex; align-items: center; gap: 10px; }
  .brand-name { font-family: "Ubuntu", sans-serif; font-weight: 700; font-size: 46px; letter-spacing: -1px; color: var(--ink); line-height: 1; }
  .brand-mark { width: 30px; height: 30px; background: var(--t-flame); }

  .search { position: absolute; left: 453px; top: 36px; width: 299px; height: 37px; display: flex; border-radius: 3px; overflow: hidden; box-shadow: 0 1px 3px rgba(0,0,0,0.2); }
  .search-field { flex: 1; background: var(--search-bg); border: 0; padding-left: 15px; font: 400 13px "Open Sans", sans-serif; color: #999; display: flex; align-items: center; }
  .search-btn { width: 41px; background: var(--search-btn); display: flex; align-items: center; justify-content: center; }

  .main-nav { position: absolute; left: 779px; top: 45px; font: 400 14px "Open Sans", sans-serif; display: flex; gap: 12px; }
  .login-btn { position: absolute; left: 979px; top: 37px; width: 92px; height: 35px; border: 2px solid var(--ink); border-radius: 3px; display: flex; align-items: center; justify-content: center; font: 600 16px "Open Sans", sans-serif; }

  .headline { position: absolute; top: 154px; left: 0; width: 1200px; text-align: center; font: 700 26px "Ubuntu", sans-serif; letter-spacing: -0.3px; }

  .feed-panel { position: absolute; left: 322px; top: 200px; width: 549px; height: 491px; background: var(--panel); border-radius: 3px; box-shadow: 0 2px 8px rgba(0,0,0,0.35); color: #fff; }
  .feed-title { position: absolute; top: 20px; width: 100%; text-align: center; font: 700 26px "Ubuntu", sans-serif; letter-spacing: -0.3px; }
  .category-grid { position: absolute; left: 29px; top: 71px; width: 493px; height: 315px; display: grid; grid-template-columns: repeat(5, 1fr); grid-template-rows: repeat(4, 1fr); }
  .tile { display: flex; flex-direction: column; align-items: center; justify-content: flex-end; padding-bottom: 8px; text-align: center; font: 400 12px/1.2 "Ubuntu", sans-serif; text-transform: uppercase; color: #fff; }
  .tile svg { width: 34px; height: 34px; margin-bottom: 5px; fill: #fff; }
  .tile.member { justify-content: center; font-size: 13px; padding-bottom: 0; }
  .join-btn { margin-top: 7px; background: var(--join); color: #222; text-transform: none; font: 500 11px "Ubuntu", sans-serif; padding: 3px 10px; border-radius: 2px; }

  .slogan { position: absolute; top: 397px; width: 100%; text-align: center; font: 700 26px "Ubuntu", sans-serif; letter-spacing: -0.3px; }
  .connect-row { position: absolute; top: 444px; left: 114px; display: flex; align-items: center; gap: 10px; font: 400 12px Arial, sans-serif; }
  .connect-btn { width: 185px; height: 29px; background: var(--friendora); display: flex; align-items: center; border-radius: 2px; }
  .connect-btn .sq { width: 29px; height: 29px; background: rgba(255,255,255,0.12); border-right: 1px solid rgba(0,0,0,0.2); }
  .connect-btn span { flex: 1; text-align: center; font: 700 12px Arial, sans-serif; color: #fff; }
  .sign-in { color: var(--link-blue); font-weight: 700; }

  .site-footer { position: absolute; left: 0; top: 823px; width: 1200px; height: 55px; background: var(--footer); display: flex; align-items: center; justify-content: center; gap: 8px; font: 400 13px "Open Sans", sans-serif; color: #fff; }
</style>
</head>
<body>
  <div class="backdrop" role="img" aria-label="Bright city skyline behind glass with shoppers carrying bags walking on a reflective floor"></div>

  <header class="site-header">
    <div class="brand"><span class="brand-name">TrindaMo</span><span class="brand-mark"></span></div>
    <div class="search">
      <div class="search-field">Search</div>
      <div class="search-btn">
        <svg width="18" height="18" viewBox="0 0 18 18"><circle cx="7" cy="7" r="5" fill="none" stroke="#222" stroke-width="2.4"/><line x1="10.8" y1="10.8" x2="16" y2="16" stroke="#222" stroke-width="3" stroke-linecap="round"/></svg>
      </div>
    </div>
    <nav class="main-nav"><span>HOW IT WORKS</span><span>|</span><span>BUSINESS</span></nav>
    <div class="login-btn">LOGIN</div>
  </header>

  <h1 class="headline">SHOP DIRECTLY FROM YOUR PROFILE</h1>

  <section class="feed-panel">
    <h2 class="feed-title">SETUP YOUR FEED</h2>
    <div class="category-grid">
      <div class="tile" style="background:var(--t-crimson)"><svg viewBox="0 0 34 34"><circle cx="22" cy="6" r="3.5"/><path d="M10 14l7-4 5 3-3 7 5 4-2 2-7-5 2-6-3 1-3 3z M14 22l-6 8-2-2 5-7z"/></svg>Active Life</div>
      <div class="tile" style="background:var(--t-blue)"><svg viewBox="0 0 34 34"><rect x="10" y="3" width="2" height="10"/><rect x="13" y="3" width="2" height="10"/><rect x="11" y="12" width="3" height="19"/><path d="M21 3c4 0 4 10 1 12v16h-3V3z"/></svg>Food</div>
      <div class="tile" style="background:var(--t-amber)"><svg viewBox="0 0 34 34"><path d="M5 22a12 12 0 0 1 24 0v6H5z"/><circle cx="17" cy="10" r="3"/></svg>Automotive</div>
      <div class="tile" style="background:var(--t-orange)"><svg viewBox="0 0 34 34"><circle cx="14" cy="8" r="4"/><rect x="4" y="22" width="26" height="4"/><path d="M8 22l4-9 6 2 6 7z"/></svg>Beauty &amp; Spa</div>
      <div class="tile" style="background:var(--t-tan)"><svg viewBox="0 0 34 34"><path d="M2 12l15-7 15 7-15 7z M8 16v8c6 4 12 4 18 0v-8l-9 4z"/></svg>Education</div>

      <div class="tile" style="background:var(--t-periwinkle)"><svg viewBox="0 0 34 34"><path d="M4 7h26v23H4z M6 12v16h22V12z" fill-rule="evenodd"/><rect x="9" y="15" width="4" height="3"/><rect x="15" y="15" width="4" height="3"/><rect x="21" y="15" width="4" height="3"/><rect x="9" y="21" width="4" height="3"/><rect x="15" y="21" width="4" height="3"/></svg>Event Planing<br>&amp; Services</div>
      <div class="tile" style="background:var(--t-olive)"><svg viewBox="0 0 34 34"><circle cx="20" cy="11" r="8"/><path d="M3 24h8l6 3 8-4 3 2-11 7-14-3z"/></svg>Financial<br>Services</div>
      <div class="tile" style="background:var(--t-violet)"><svg viewBox="0 0 34 34"><path d="M6 6h22v16H6z M8 8v12h18V8z" fill-rule="evenodd"/><path d="M11 22l-3 9h2l3-9z M23 22l3 9h-2l-3-9z"/></svg>Art &amp;<br>Entertainment</div>
      <div class="tile" style="background:var(--t-red)"><svg viewBox="0 0 34 34"><path d="M22 4c3 0 5 3 3 6l-5 5-5-5c-2-3 0-6 3-6 1 0 2 1 2 1s1-1 2-1z"/><path d="M3 22h8l6 3 8-4 3 2-11 7-14-3z"/></svg>Health &amp;<br>Medical</div>
      <div class="tile" style="background:var(--t-mustard)"><svg viewBox="0 0 34 34"><circle cx="13" cy="20" r="8"/><circle cx="23" cy="10" r="6"/></svg>Local<br>Services</div>

      <div class="tile" style="background:var(--t-copper)"><svg viewBox="0 0 34 34"><path d="M9 8h16v23H9z"/></svg>Hotels</div>
      <div class="tile" style="background:var(--t-gold)"><svg viewBox="0 0 34 34"><path d="M17 3l15 13h-4v14H6V16H2z"/></svg>Home Services</div>
      <div class="tile" style="background:var(--t-moss)"><svg viewBox="0 0 34 34"><path d="M4 9h26v20H4z M7 12v14h20V12z" fill-rule="evenodd"/></svg>Mass Media</div>
      <div class="tile" style="background:var(--t-navy)"><svg viewBox="0 0 34 34"><path d="M7 18h20l-3 12H10z"/><circle cx="17" cy="9" r="4"/></svg>Night Life</div>
      <div class="tile" style="background:var(--t-salmon)"><svg viewBox="0 0 34 34"><path d="M8 31V18c0-6 4-9 8-9l2-5 2 5h4v22z"/></svg>Pets</div>

      <div class="tile" style="background:var(--t-coral)"><svg viewBox="0 0 34 34"><path d="M14 4l12 10h-3v14H5V14H2z"/></svg>Real Estate</div>
      <div class="tile" style="background:var(--t-flame)"><svg viewBox="0 0 34 34"><circle cx="13" cy="10" r="5"/><path d="M4 30c0-8 4-13 9-13s9 5 9 13z"/><rect x="20" y="15" width="12" height="2"/></svg>Restaurants</div>
      <div class="tile" style="background:var(--t-indigo)"><svg viewBox="0 0 34 34"><circle cx="8" cy="8" r="4"/><circle cx="17" cy="8" r="4"/><circle cx="26" cy="8" r="4"/><path d="M2 26v-8c0-3 12-3 12 0v8z M11 28v-8c0-3 12-3 12 0v8z M20 26v-8c0-3 12-3 12 0v8z"/></svg>Proessional<br>Services</div>
      <div class="tile" style="background:var(--t-bronze)"><svg viewBox="0 0 34 34"><path d="M9 5h16v18H9z M11 8v7h12V8z" fill-rule="evenodd"/><path d="M11 25l-3 6h3l2-4h8l2 4h3l-3-6z"/></svg>Public Servces<br>&amp; Government</div>
      <div class="tile member" style="background:var(--t-rose)">Become a<br>Member<span class="join-btn">Join Now</span></div>
    </div>

    <h2 class="slogan">SAVE YOUR TIME LIVE BETTER</h2>
    <div class="connect-row">
      <div class="connect-btn"><div class="sq"></div><span>Connect with Friendora</span></div>
      <div>or <span class="sign-in">Sign In</span> by default way</div>
    </div>
  </section>

  <footer class="site-footer">
    <span>About us</span><span>|</span><span>Blog</span><span>|</span><span>Business</span><span>|</span><span>Jobs</span><span>|</span><span>Privacy</span><span>|</span><span>Faq’s</span><span>|</span><span>Contact Us</span>
  </footer>
</body>
</html>
```